Business cards and stationery for new company logo
TRV Enterprises
Business cards and stationery for new company logo - Construction
Creative Brief
Simple
Marcus Pellham
Owner
742 Wildrow Ave. Alderwick, Manitoba K4T 2B5
marcus@trventerprises.ca
www.trventerprises.ca
Would like something sleek and corporate looking. Catchy. The logo that was designed has all those elements...I would like the bus cards and stationery to also have those.

```html
<!DOCTYPE html>
<html lang="en">
<head>
<meta charset="utf-8">
<title>TRV Enterprises – Business Cards</title>
<link rel="stylesheet" href="https://fonts.googleapis.com/css2?family=Open+Sans:wght@400;600;800&display=swap">
<style>
  :root {
    --backdrop: #e6e6e6;
    --card-white: #fbfbfb;
    --card-black: #0c0c0c;
    --ink: #2b2b2b;
    --ink-soft: #555555;
    --accent-red: #d8322c;
    --rule: #3a3a3a;
    --rule-soft: #bdbdbd;
  }
  * { margin: 0; padding: 0; box-sizing: border-box; }
  html, body {
    width: 1200px; height: 901px; overflow: hidden;
    background: var(--backdrop);
    font-family: "Open Sans", Arial, sans-serif;
  }
  .stage { position: relative; width: 1200px; height: 901px; }

  .card {
    position: absolute;
    width: 560px; height: 320px;
    box-shadow: 0 10px 28px rgba(0,0,0,.22);
  }

  .wordmark {
    font-weight: 800;
    letter-spacing: 1px;
    line-height: 1;
    text-transform: uppercase;
    white-space: nowrap;
  }

  /* Back side */
  .card-back {
    left: 110px; top: 80px;
    background: var(--card-black);
    display: flex; flex-direction: column;
    align-items: center; justify-content: center;
  }
  .card-back .wordmark { color: #ffffff; font-size: 46px; }
  .card-back .web {
    margin-top: 12px;
    color: var(--accent-red);
    font-size: 15px; letter-spacing: .5px;
  }

  /* Front side */
  .card-front {
    left: 530px; top: 480px;
    background: var(--card-white);
  }
  .card-front .wordmark {
    position: absolute; left: 44px; top: 46px;
    color: var(--ink); font-size: 38px;
  }
  .divider-h {
    position: absolute; left: 20px; right: 20px; top: 192px;
    height: 1px; background: var(--rule);
  }
  .address {
    position: absolute; left: 30px; top: 198px;
    width: 116px;
    font-style: normal;
    font-size: 13px; line-height: 18px; color: var(--ink);
  }
  .divider-v {
    position: absolute; left: 150px; top: 196px;
    width: 1px; height: 96px; background: var(--rule);
  }
  .contacts {
    position: absolute; left: 160px; top: 200px;
    list-style: none;
    font-size: 13px; color: var(--ink);
  }
  .contacts li {
    width: 190px;
    padding: 2px 0;
    border-bottom: 1px solid var(--rule-soft);
  }
  .contacts .label { color: var(--accent-red); font-weight: 600; margin-right: 3px; }
  .person {
    position: absolute; right: 30px; top: 236px;
    text-align: right;
  }
  .person .name { color: var(--accent-red); font-weight: 600; font-size: 17px; }
  .person .role {
    width: 160px; margin: 4px 0 0 auto; padding-top: 3px;
    border-top: 1px solid var(--rule);
    font-size: 12px; color: var(--ink-soft);
  }
</style>
</head>
<body>
<main class="stage">
  <section class="card card-back" aria-label="Business card back">
    <div class="wordmark">TRV Enterprises</div>
    <div class="web">www.trventerprises.ca</div>
  </section>

  <section class="card card-front" aria-label="Business card front">
    <div class="wordmark">TRV Enterprises</div>
    <div class="divider-h"></div>
    <address class="address">
      742 Wildrow Ave.<br>Alderwick, Manitoba<br>K4T 2B5
    </address>
    <div class="divider-v"></div>
    <ul class="contacts">
      <li><span class="label">C :</span>613-555-0148</li>
      <li><span class="label">E :</span>marcus@trventerprises.ca</li>
      <li><span class="label">W :</span>www.trventerprises.ca</li>
    </ul>
    <div class="person">
      <div class="name">Marcus Pellham</div>
      <div class="role">Owner</div>
    </div>
  </section>
</main>
</body>
</html>
```